we are a small based family business that specialise in 12v led lights for tarvin caravans.
we also sell 12v switches, wire, circuit breakers, dimmers etc but our main line is LEDs.
We would like something that reflects the LED lighting on our cards.
www.reefcrestlamps.example.au is where you can have a look at to get ideas, of our product.
I have attached the logo we generally use on all our shopra listings and is the main header on our website.

Look forward to seeing what your team comes up with.

Business

Tam 0491 738 205
Corrawin Vale QLD 4391

www.reefcrestlamps.example

```html
<!DOCTYPE html>
<html lang="en">
<head>
<meta charset="utf-8">
<title>Reefcrest Lamps – Business Card</title>
<link rel="stylesheet" href="https://fonts.googleapis.com/css2?family=Open+Sans:wght@400;800&display=swap">
<style>
  :root {
    --backdrop: #2b2b2b;
    --band-blue: #1276bd;
    --band-blue-light: #4a9bd3;
    --card-white: #ffffff;
    --brand-red: #b42a23;
    --text-white: #ffffff;
  }
  html, body {
    margin: 0;
    padding: 0;
    width: 1200px;
    height: 849px;
    overflow: hidden;
    background: var(--backdrop);
  }
  .canvas {
    position: relative;
    width: 1200px;
    height: 849px;
  }
  .business-card {
    position: absolute;
    left: 150px;
    top: 168px;
    width: 900px;
    height: 514px;
    border-radius: 28px;
    background: var(--card-white);
    overflow: hidden;
    box-shadow: 0 18px 40px rgba(0, 0, 0, 0.45);
  }
  .blue-band {
    position: absolute;
    left: 0;
    top: 0;
    width: 100%;
    height: 318px;
    background: var(--band-blue);
  }
  .contact-details {
    position: absolute;
    left: 72px;
    top: 88px;
    margin: 0;
    font-family: "Open Sans", Arial, sans-serif;
    font-weight: 400;
    font-size: 27px;
    line-height: 1.28;
    color: var(--text-white);
    font-style: normal;
  }
  .contact-details span { display: block; }
  .light-glow {
    position: absolute;
    right: 20px;
    top: 28px;
    width: 360px;
    height: 270px;
  }
  .brand-name {
    position: absolute;
    left: 0;
    right: 0;
    top: 388px;
    margin: 0;
    text-align: center;
    font-family: "Open Sans", Arial, sans-serif;
    font-weight: 800;
    font-size: 46px;
    letter-spacing: 0.5px;
    color: var(--brand-red);
  }
</style>
</head>
<body>
<main class="canvas">
  <section class="business-card">
    <div class="blue-band"></div>
    <address class="contact-details">
      <span>Tam 0491 738 205</span>
      <span>Corrawin Vale QLD 4391</span>
      <span>www.reefcrestlamps.example</span>
    </address>
    <svg class="light-glow" viewBox="0 0 360 270" role="img" aria-label="Pattern of soft glowing LED light dots fanning outward">
      <defs>
        <radialGradient id="glowFill" cx="70%" cy="50%" r="70%">
          <stop offset="0%" stop-color="var(--band-blue-light)" stop-opacity="0.75"/>
          <stop offset="100%" stop-color="var(--band-blue)" stop-opacity="0"/>
        </radialGradient>
      </defs>
      <rect width="360" height="270" rx="40" fill="url(#glowFill)"/>
    </svg>
    <h1 class="brand-name">Reefcrest Lamps</h1>
  </section>
</main>
</body>
</html>
```